Invitation for a charity event - Plum Falcon - 5 x 7 inches

This is an event held at Vista Loma Raceway in San Diego, California. This invitation can have any theme related to horseracing, the beach or even Lew Hartwell, who was a founder of Vista Loma.

here is the content of the invitation:
Hold your horses....
Plum Falcon 21 will be here on August 22nd!

This fine event started as just a thought,
between the two great minds of "Plum" and "the Falcon."
They said, "Let's get 20 guys in a Vista Loma suite,"
with beer, Bastien Roux and plenty to eat.
21 years ago they made it happen,
When Walt started singing, toes would be tappin'
The ticket was so hot, there was a waiting list,
And for this spectacular event no one would miss.
Fast forward to the present and look how it's evolved.
How it got to epic status is a puzzle yet to be solved.
One things for certain and I can say this so loud,
ALL OF THE FALLEN FALCONS WOULD BE SO PROUD!

Thursday, August 22nd, 12:30 pm. Lunch served at 1:00
Vista Loma Raceway, Paddock Lounge Suite P
RSVP: Nora Quimby - norapemberton47@mailvale.test
(415) 555-0187
* Men, sports coat required

Target Market(s)

Men and women

Colors

Designer to choose colors to be used in the design.

Requirements
Must have
• All the content above must be included. Invitation should be 5 x 7 inches
• ***the logo I've included can be used in the invitation but doesn't have to be used. If it is used, please change the 20 to 21***** Thank you!

```html
<!DOCTYPE html>
<html lang="en">
<head>
<meta charset="utf-8">
<title>Plum Falcon 21 Invitation</title>
<link href="https://fonts.googleapis.com/css2?family=Roboto:wght@700;900&family=Roboto+Condensed:wght@400;700&display=swap" rel="stylesheet">
<style>
  :root {
    --panel-top: #2e2e2e;
    --panel-bottom: #050505;
    --ink-white: #ffffff;
    --ink-soft: #d4d4d4;
    --rule: #8a8a8a;
  }
  * { margin: 0; padding: 0; box-sizing: border-box; }
  html, body { width: 1200px; height: 857px; overflow: hidden; background: #000; }
  .invitation {
    position: relative; width: 1200px; height: 857px; overflow: hidden;
    background: linear-gradient(180deg, var(--panel-top) 0%, #1a1a1a 45%, var(--panel-bottom) 100%);
    font-family: "Roboto Condensed", "Arial Narrow", sans-serif;
    color: var(--ink-white);
  }
  .race-art { position: absolute; inset: 0; width: 1200px; height: 857px; }
  .brand {
    position: absolute; left: 76px; top: 74px; display: flex; align-items: center; gap: 14px;
    font-weight: 700; font-size: 40px; letter-spacing: 1px; color: var(--ink-white); text-transform: uppercase;
    white-space: nowrap;
  }
  .brand-dot { width: 22px; height: 22px; border-radius: 50%; background: var(--ink-white); }
  .story {
    position: absolute; left: 72px; top: 206px; width: 440px;
    font-size: 17.8px; line-height: 22.8px; color: var(--ink-soft); white-space: nowrap;
  }
  .story p + p { margin-top: 22.8px; }
  .event-date { position: absolute; left: 72px; top: 548px; font-weight: 700; white-space: nowrap; }
  .event-date .day { font-size: 28px; line-height: 32px; }
  .event-date .day sup { font-size: 15px; }
  .event-date .time { font-size: 22px; line-height: 28px; }
  .divider { position: absolute; left: 70px; top: 620px; width: 410px; height: 1px; background: var(--rule); }
  .venue { position: absolute; left: 70px; top: 636px; white-space: nowrap; }
  .venue .place { font-weight: 700; font-size: 21px; line-height: 28px; }
  .venue .dress { font-size: 21px; line-height: 32px; }
  .rsvp { position: absolute; left: 70px; top: 712px; display: flex; gap: 20px; white-space: nowrap; }
  .rsvp-label { font-weight: 700; font-size: 40px; line-height: 48px; }
  .rsvp-details { font-size: 21px; line-height: 28.5px; padding-top: 4px; }
  .rsvp-details .strong { font-weight: 700; }
  .headline, .announce {
    position: absolute; font-family: "Roboto", Arial, sans-serif;
    text-align: center; text-transform: uppercase; color: var(--ink-white);
    text-shadow: 2px 3px 4px rgba(0,0,0,.75); white-space: nowrap;
  }
  .headline { left: 800px; width: 348px; top: 64px; line-height: .9; font-weight: 900; }
  .headline .small { display: block; font-size: 60px; }
  .headline .big { display: block; font-size: 80px; }
  .announce { left: 700px; width: 472px; top: 528px; font-weight: 700; }
  .announce .name { display: block; font-size: 54px; line-height: 58px; }
  .announce .here { display: block; font-size: 36px; line-height: 40px; }
  .announce .date { display: block; font-size: 56px; line-height: 72px; }
  .announce .date .on { font-size: 30px; }
  .announce .date sup { font-size: 28px; }
</style>
</head>
<body>
<main class="invitation">
  <svg class="race-art" viewBox="0 0 1200 857">
    <defs>
      <linearGradient id="photoTone" x1="0" y1="0" x2="0" y2="1">
        <stop offset="0" stop-color="#3c6a63"/>
        <stop offset=".3" stop-color="#4a5a3e"/>
        <stop offset=".55" stop-color="#5a3424"/>
        <stop offset=".8" stop-color="#3a2a1e"/>
        <stop offset="1" stop-color="#6d8f4a"/>
      </linearGradient>
      <radialGradient id="silkGlow" cx=".6" cy=".4" r=".5">
        <stop offset="0" stop-color="#b42a2a" stop-opacity=".45"/>
        <stop offset="1" stop-color="#b42a2a" stop-opacity="0"/>
      </radialGradient>
    </defs>
    <path d="M800 0 C500 140 380 560 744 857" fill="none" stroke="#ffffff" stroke-width="14" stroke-opacity=".9"/>
    <g role="img" aria-label="Photograph of jockeys in bright silks racing thoroughbred horses head-on across a turf track">
      <path d="M810 0 C512 140 392 560 754 857 L1200 857 L1200 0 Z" fill="url(#photoTone)"/>
      <path d="M810 0 C512 140 392 560 754 857 L1200 857 L1200 0 Z" fill="url(#silkGlow)"/>
    </g>
  </svg>

  <div class="brand"><span class="brand-dot"></span>Plum Falcon 21</div>

  <section class="story">
    <p>This fine event started as just a crazy thought,<br>between the two great minds of "Plum" and<br>"The Falcon" They said, lets get 20 guys in a Vista Loma<br>suite, with beer, Bastien Roux and plenty to eat</p>
    <p>21 years ago they made it happen,<br>when Walt started singing, the toes started tappin'<br>The ticket was so hot, there was a waiting list,<br>and on this spectacular day, nobody would miss.</p>
    <p>Fast forward to present and look how its evolved,<br>How it got to epic status is a puzzle yet to be solved.<br>One thing is for certain, and I can say this quite loud,<br>ALL OF THE FALLEN FALCONS WOULD BE SO PROUD!</p>
  </section>

  <div class="event-date">
    <div class="day">Thursday, August 22<sup>nd</sup>,</div>
    <div class="time">12:30 pm. Lunch served at 1:00</div>
  </div>
  <div class="divider"></div>
  <div class="venue">
    <div class="place">Vista Loma Raceway, Paddock Lounge Suite P</div>
    <div class="dress">* Men, sports coat required</div>
  </div>
  <div class="rsvp">
    <div class="rsvp-label">RSVP:</div>
    <div class="rsvp-details">
      <div class="strong">Nora Quimby</div>
      <div>norapemberton47@mailvale.test</div>
      <div class="strong">(415) 555-0187</div>
    </div>
  </div>

  <h1 class="headline"><span class="small">Hold Your</span><span class="big">Horses</span></h1>
  <div class="announce">
    <span class="name">Plum Falcon 21</span>
    <span class="here">Will be here</span>
    <span class="date"><span class="on">On </span>August 22<sup>nd</sup>!</span>
  </div>
</main>
</body>
</html>
```